Harlow Terrain Consultants
Business Card and Stationary Design
Professional
Paul Dorrick, PE
4259 Copper Fern Lane
Fairbrook, Texas 75412
paul@harlow-terrain.com

```html
<!DOCTYPE html>
<html lang="en">
<head>
<meta charset="UTF-8">
<title>Harlow Terrain Consultants – Business Card</title>
<link rel="stylesheet" href="https://fonts.googleapis.com/css2?family=Arimo:wght@400&display=swap">
<style>
  :root {
    --paper: #ffffff;
    --blue-light: #4a8fd0;
    --blue-mid: #2f6cb0;
    --blue-deep: #1a3c78;
    --stripe-green: #1f4a1c;
    --brand-green: #5f8a2b;
    --brand-mark: #6d9a34;
    --card-text: #ffffff;
  }
  * { margin: 0; padding: 0; box-sizing: border-box; }
  html, body {
    width: 1200px;
    height: 718px;
    overflow: hidden;
    background: var(--paper);
  }
  .card {
    position: relative;
    width: 1200px;
    height: 718px;
    background: var(--paper);
    font-family: "Arimo", Arial, sans-serif;
    overflow: hidden;
  }
  .card-panel {
    position: absolute;
    inset: 0;
    width: 1200px;
    height: 718px;
  }
  .brand {
    position: absolute;
    left: 40px;
    top: 228px;
    width: 544px;
    text-align: center;
    color: var(--brand-green);
    font-weight: 400;
  }
  .brand-dot {
    display: block;
    width: 132px;
    height: 132px;
    margin: 0 auto 48px;
    border-radius: 50%;
    background: var(--brand-mark);
  }
  .brand-name {
    font-size: 40px;
    line-height: 1.15;
    letter-spacing: 0.5px;
  }
  .brand-name .brand-sub {
    display: block;
    font-size: 22px;
    letter-spacing: 7px;
    margin-top: 6px;
  }
  .contact {
    position: absolute;
    left: 714px;
    top: 0;
    width: 486px;
    height: 718px;
    color: var(--card-text);
    font-weight: 400;
  }
  .contact-name {
    position: absolute;
    top: 192px;
    left: 0;
    width: 410px;
    text-align: center;
    white-space: nowrap;
    font-size: 41px;
    font-weight: 400;
  }
  .contact-lines {
    position: absolute;
    top: 362px;
    left: 0;
    width: 348px;
    text-align: center;
    white-space: nowrap;
    font-size: 28px;
    line-height: 41px;
  }
  .contact-lines .gap { margin-top: 26px; }
</style>
</head>
<body>
  <div class="card">
    <svg class="card-panel" viewBox="0 0 1200 718" aria-hidden="true">
      <defs>
        <linearGradient id="panelBlue" x1="0" y1="0" x2="1" y2="0">
          <stop offset="0" stop-color="var(--blue-light)"/>
          <stop offset="0.45" stop-color="var(--blue-mid)"/>
          <stop offset="1" stop-color="var(--blue-deep)"/>
        </linearGradient>
      </defs>
      <path class="panel-stripe" d="M744 0 C640 180 566 450 554 718 L582 718 C592 450 662 180 760 0 Z" fill="var(--stripe-green)"/>
      <path class="panel-fill" d="M760 0 C662 180 592 450 582 718 L1200 718 L1200 0 Z" fill="url(#panelBlue)"/>
    </svg>

    <div class="brand">
      <span class="brand-dot"></span>
      <p class="brand-name">HARLOW TERRAIN<span class="brand-sub">CONSULTANTS</span></p>
    </div>

    <div class="contact">
      <h1 class="contact-name">Paul Dorrick, PE</h1>
      <div class="contact-lines">
        <p>4259 Copper Fern Lane</p>
        <p>Fairbrook, Texas 75412</p>
        <p class="gap">Phone : 214-555-0142</p>
        <p>Cell : 214-555-0187</p>
        <p class="gap">Email : paul@harlow-terrain.com</p>
      </div>
    </div>
  </div>
</body>
</html>
```